Email signature design - law firm

We are a small boutique law firm which is located near the beach in Manly, Australia.

We have just recently developed a new logo and are looking to redesign our letterhead, business cards and email signatures.

This brief is for our email signatures. This is an email signature to appear at the bottom of our Outlook emails so we would like it to be text that we are able to edit as the wording in our email signature often required amendments.

I have attached a word document which had our new logo, and our previous email signature which all the information/wording that needs to be included.

We would like multiple designs with a modern, simplistic yet striking look.

Thanks.

font - raleway or montserrat

Need extra days to review

• Must have the exact wording which appears in the email signature in the word document attached to brief.
• Must be able to edit the text as it is for an Outlook email signature which wording will change from time to time.

```html
<!DOCTYPE html>
<html lang="en">
<head>
<meta charset="utf-8">
<title>Corwell &amp; Partners – Email Signature</title>
<link rel="stylesheet" href="https://fonts.googleapis.com/css2?family=Montserrat:wght@500;600;700&display=swap">
<style>
  :root {
    --ink: #111111;
    --paper: #ffffff;
  }
  html, body {
    margin: 0;
    padding: 0;
    overflow: hidden;
    background: var(--paper);
  }
  .signature {
    position: relative;
    width: 1200px;
    height: 602px;
    overflow: hidden;
    background: var(--paper);
    color: var(--ink);
    font-family: "Montserrat", sans-serif;
    font-weight: 500;
  }
  .signature > * {
    position: absolute;
    left: 49px;
    margin: 0;
    white-space: nowrap;
  }
  .sign-off { top: 81px; font-size: 15px; line-height: 20px; }
  .sender-name { top: 103px; font-size: 19px; line-height: 24px; font-weight: 700; }
  .contact { top: 140px; font-size: 15px; line-height: 22.6px; font-style: normal; }
  .contact .firm-name { font-weight: 700; }
  .contact span { display: block; }
  .contact .locality { word-spacing: 14px; }
  .notice {
    font-size: 13.6px;
    line-height: 17px;
    letter-spacing: 0.05px;
  }
  .notice span { display: block; }
  .notice-privilege { top: 284px; }
  .notice-unauthorised { top: 352px; }
  .notice-liability { top: 386px; }
  .notice-fraud { top: 454px; }
</style>
</head>
<body>
  <div class="signature">
    <p class="sign-off">Regards,</p>
    <p class="sender-name">Maren Holloway</p>
    <address class="contact">
      <span class="firm-name">Corwell &amp; Partners</span>
      <span>Suite 4, 18 Pelican Lane</span>
      <span class="locality">FAIRLIGHT NSW 2094</span>
      <span>Ph: (02) 9410 3680</span>
      <span>Fax: (02) 9410 3681</span>
      <span>www.corwellpartners.com.au</span>
    </address>
    <p class="notice notice-privilege">
      <span>Important note: This E-Mail and any attachment is PRIVILEGED and confidential.&nbsp; It must not be read, copied, disclosed or used by any person</span>
      <span>other than the above named addressees.&nbsp; In order to preserve the intended confidentiality and privilege, please notify us immediately if you</span>
      <span>have received this e-mail by mistake and secure-delete this e-mail from your system.</span>
    </p>
    <p class="notice notice-unauthorised">Unauthorised perusal, use, disclosure, forwarding or copying is strictly prohibited and may be unlawful.</p>
    <p class="notice notice-liability">
      <span>Liability limited by a scheme approved under Professional Standards Legislation. Legal practitioners at HarbourLaw (NSW) Pty Ltd are members of</span>
      <span>the scheme.</span>
    </p>
    <p class="notice notice-fraud">
      <span>Fraud warning: Please be aware that there is a significant risk posed by cyber fraud, specifically relating to email accounts and bank account</span>
      <span>details. Our bank account details will never change during the course of a transaction, and we will never advise you of a change to our bank</span>
      <span>details via email.&nbsp; Please check account details with us in person or by phone before making payments.&nbsp; If you advise us of your bank</span>
      <span>account details by email, please also ring and confirm the bank account details by phone as well.</span>
    </p>
  </div>
</body>
</html>
```